Mellow Truffles. We need a website as delcious as our chocolate.

I need a website to promote our humble chocolate business. We our proud of are chocolate because we use only our favorite ingredients. We believe in originality and complete enjoyment of our chocolates. I am looking for a sleek and smooth website. I would like to see typical pages such as contact information and an intro. I would like to have a product page, which can be easily updated with photos of new chocolate. I would also like to see a page where we can educate customers about chocolate. This might be tricky but I would like our customers to leave the site knowing they are getting great chocolate! I have a logo and general color scheme, which I will try to upload somewhere. I looking for an original and exciting website.
Updates

Websites we like:

1. http://www.paul-van-orlen.example/ (looks really good)

2. http://www.tremilcocoa.example/

uploaded logo !

Target Market(s)

People who enjoy chocolate.

Industry/Entity Type

Business

Requirements
Must have
• User Friendly
Page were pictures of new chocolate can be easily updated.

Nice to have
• Calming and appetizing music
Section where recent tweets can show up on the site.

```html
<!DOCTYPE html>
<html lang="en">
<head>
<meta charset="utf-8">
<title>Mellow Truffles — Homemade with passion</title>
<link rel="stylesheet" href="https://fonts.googleapis.com/css2?family=Arimo:wght@400;700&family=Open+Sans:wght@400;600&family=Lora:ital@1&display=swap">
<style>
  :root {
    --cocoa: #4a1408;
    --brown-panel: #8b4a33;
    --pink-panel: #f3c7d7;
    --pink-footer: #f3e1e9;
    --pink-icon: #e67aa6;
    --link-plum: #a2285e;
    --nav-text: #e8b9a8;
    --body-grey: #6f6a6a;
    --copy-grey: #b79aa8;
    --white: #ffffff;
  }
  * { box-sizing: border-box; margin: 0; padding: 0; }
  html, body { width: 1200px; height: 958px; overflow: hidden; background: var(--white); }
  body { position: relative; font-family: "Arimo", Arial, sans-serif; }

  .hero {
    position: absolute; left: 0; top: 0; width: 1200px; height: 460px;
    background:
      radial-gradient(ellipse 320px 260px at 700px 300px, rgba(80,20,30,.85), rgba(80,20,30,0) 70%),
      linear-gradient(90deg, #f4cde0 0%, #f0bcd5 22%, #e8b0c6 40%, #7a3042 55%, #5a2030 68%, #8a5d66 84%, #b9959c 100%);
  }
  .site-header {
    position: absolute; left: 0; top: 10px; width: 1200px; height: 56px;
    background: rgba(236, 200, 220, .45);
  }
  .brand {
    position: absolute; left: 22px; top: 16px;
    font-family: "Arimo", Arial, sans-serif; font-size: 20px; font-weight: 700;
    color: var(--cocoa); letter-spacing: .5px;
  }
  .main-nav { position: absolute; right: 136px; top: 20px; display: flex; gap: 20px; }
  .main-nav a {
    font-size: 14px; color: var(--nav-text); text-decoration: none; letter-spacing: .2px;
  }

  .section-title {
    position: absolute; font-size: 16px; font-weight: 400; color: var(--cocoa); letter-spacing: .2px;
  }
  .feed-title { left: 127px; top: 487px; }
  .welcome-title { left: 467px; top: 487px; }

  .feed {
    position: absolute; left: 127px; top: 521px; width: 276px; height: 352px;
    background: var(--brown-panel); border-radius: 5px;
    font-family: "Open Sans", Arial, sans-serif;
  }
  .feed-profile { position: absolute; left: 10px; top: 10px; display: flex; gap: 8px; }
  .feed-avatar { width: 31px; height: 31px; background: linear-gradient(135deg, #e9e4e0, #6e6460); border: 1px solid #fff; }
  .feed-name { font-size: 10px; color: #e3bfb0; line-height: 12px; margin-top: 1px; }
  .feed-handle { font-size: 15px; font-weight: 600; color: #e3bfb0; line-height: 18px; }
  .feed-list {
    position: absolute; left: 1px; top: 51px; width: 274px; height: 266px;
    background: var(--pink-panel); border-radius: 5px; list-style: none; padding: 0 8px;
  }
  .tweet { padding: 6px 0 4px; border-bottom: 1px solid #e5b3c5; font-size: 11.6px; line-height: 14px; color: #2c1a1a; }
  .tweet:last-child { border-bottom: 0; }
  .tweet-user, .tweet a { color: var(--link-plum); text-decoration: none; }
  .tweet-meta { display: block; font-size: 8.5px; color: var(--link-plum); margin-top: 1px; }
  .feed-footer { position: absolute; left: 10px; right: 10px; bottom: 7px; display: flex; justify-content: space-between; align-items: center; }
  .feed-join { font-size: 11.5px; color: #e3bfb0; }

  .welcome-text {
    position: absolute; left: 467px; top: 521px; width: 596px;
    font-size: 11.4px; line-height: 13.8px; color: var(--body-grey);
  }

  .site-footer {
    position: absolute; left: 0; top: 888px; width: 1200px; height: 70px; background: var(--pink-footer);
  }
  .footer-icon { position: absolute; top: 16px; }
  .footer-feed { left: 141px; }
  .footer-social { left: 628px; }
  .copyright {
    position: absolute; right: 142px; top: 28px;
    font-family: "Lora", Georgia, serif; font-style: italic; font-size: 11.5px; color: var(--copy-grey);
  }
</style>
</head>
<body>
  <div class="hero" role="img" aria-label="Photograph of a pink gift box beside rows of chocolate pralines in plum paper cups, with a decorative pink tree on the left"></div>

  <header class="site-header">
    <div class="brand">Mellow Truffles</div>
    <nav class="main-nav">
      <a href="#about">ABOUT US</a>
      <a href="#chocolate">OUR CHOCOLATE</a>
      <a href="#contact">CONTACT US</a>
    </nav>
  </header>

  <h2 class="section-title feed-title">FROM THE CHIRPLINE</h2>
  <aside class="feed">
    <div class="feed-profile">
      <div class="feed-avatar" role="img" aria-label="Profile photo"></div>
      <div>
        <div class="feed-name">Jordan Belmont</div>
        <div class="feed-handle">JORDANBELMONT</div>
      </div>
    </div>
    <ul class="feed-list">
      <li class="tweet"><span class="tweet-user">jordanbelmont</span> Excited to be back in Malaysia for TuneWave World Stage! But first a day off playing some games and chillin by the pool.<span class="tweet-meta">2 hours ago · reply · retweet · favorite</span></li>
      <li class="tweet"><span class="tweet-user">jordanbelmont</span> always great to see my friends at Hanabi Morning! now off to the airport. thank you japan for all your love and support!!! <a href="#">#BELIEVE</a><span class="tweet-meta">16 hours ago · reply · retweet · favorite</span></li>
      <li class="tweet"><span class="tweet-user">scottybrandt</span> great album review – <a href="#">clipit.example/ukgsMzstZYM</a><span class="tweet-meta">yesterday · reply · retweet · favorite</span></li>
      <li class="tweet"><span class="tweet-user">jordanbelmont</span> another great day in Japan. Honored to be here and grateful for the response.<span class="tweet-meta">yesterday · reply · retweet · favorite</span></li>
    </ul>
    <div class="feed-footer">
      <svg width="16" height="16" aria-hidden="true"><circle cx="8" cy="8" r="7" fill="#ffffff"/></svg>
      <span class="feed-join">Join the conversation</span>
    </div>
  </aside>

  <h1 class="section-title welcome-title">WELCOME TO MELLOW TRUFFLES</h1>
  <div class="welcome-text">
    <p>Lorem ipsum dolor sit amet, consectetur adipisicing elit, sed do eiusmod tempor incididunt ut labore et dolore magna aliqua. Ut enim ad minim veniam, quis nostrud exercitation ullamco laboris nisi ut aliquip ex ea commodo consequat. Duis aute irure dolor in reprehenderit in voluptate velit esse cillum dolore eu fugiat nulla pariatur. Excepteur sint occaecat cupidatat non proident, sunt in culpa qui officia deserunt mollit anim id est laborum.</p>
    <p>Lorem ipsum dolor sit amet, consectetur adipisicing elit, sed do eiusmod tempor incididunt ut labore et dolore magna aliqua. Ut enim ad minim veniam, quis nostrud exercitation ullamco laboris nisi ut aliquip ex ea commodo consequat. Duis aute irure dolor in reprehenderit in voluptate velit esse cillum dolore eu fugiat nulla pariatur. Excepteur sint occaecat cupidatat non proident, sunt in culpa qui officia deserunt mollit anim id est laborum.</p>
    <p>Lorem ipsum dolor sit amet, consectetur adipisicing elit, sed do eiusmod tempor incididunt ut labore et dolore magna aliqua. Ut enim ad minim veniam, quis nostrud exercitation ullamco laboris nisi ut aliquip ex ea commodo consequat. Duis aute irure dolor in reprehenderit in voluptate velit esse cillum dolore eu fugiat nulla pariatur. Excepteur sint occaecat cupidatat non proident, sunt in culpa qui officia deserunt mollit anim id est laborum.</p>
  </div>

  <footer class="site-footer">
    <svg class="footer-icon footer-feed" width="38" height="38" aria-label="News feed"><circle cx="19" cy="19" r="18" fill="var(--pink-icon)"/></svg>
    <svg class="footer-icon footer-social" width="38" height="38" aria-label="Chirpline"><circle cx="19" cy="19" r="18" fill="var(--pink-icon)"/></svg>
    <p class="copyright">© Copyright Mellow Truffles Company | 2012</p>
  </footer>
</body>
</html>
```